Halvercott Orthodontics business card

Using our existing logo (created with ArtFolio), please create a tasteful, contemporary business card. We are father and daughter orthodontists specializing in braces, clarafit, etc to design healthy, beautiful smiles for children, adolescents, and adults. We would like the design to be family-friendly but not childish.
The final design should include all of the information without looking cluttered (I hope! If necessary to achieve an optimal design, please consider making the card double-sided)
Purple, black, silver on a white card
Please include the following information:
Halvercott Orthodontics (logo)
Marguerite L. Halvercott, DMD
Douglas R. Halvercott, DMD

312 Bramblewood Street
North Andover, MA 01899
978.555.0142

847C Quarry Hollow Street
Methuen, MA 01898
978.555.0187

email frontdesk@halvercottortho.example
website www.halvercottortho.example

```html
<!DOCTYPE html>
<html lang="en">
<head>
<meta charset="UTF-8">
<title>Halvercott Orthodontics – Business Card</title>
<link href="https://fonts.googleapis.com/css2?family=Source+Sans+3:wght@400;600&display=swap" rel="stylesheet">
<style>
  :root {
    --purple: #652b91;
    --grey-text: #5a5a5a;
    --grey-muted: #8a8a8a;
    --silver: #8c8c8c;
    --white: #ffffff;
    --backdrop: #b3b3b3;
  }
  * { margin: 0; padding: 0; box-sizing: border-box; }
  html, body {
    width: 1093px; height: 1200px; overflow: hidden;
    background: var(--backdrop);
    font-family: "Source Sans 3", "Myriad Pro", sans-serif;
  }
  .card {
    position: absolute; left: 265px;
    width: 578px; height: 356px;
    border-radius: 26px; overflow: hidden;
  }
  .card--front { top: 226px; background: var(--white); }
  .card--back { top: 621px; background: var(--purple); }

  .brand {
    display: flex; align-items: center; gap: 8px;
    font-weight: 600; white-space: nowrap;
  }
  .brand__dot { border-radius: 50%; flex: none; }
  .card--front .brand {
    position: absolute; left: 20px; width: 230px; top: 144px;
    color: var(--purple); font-size: 18px;
  }
  .card--front .brand__dot { width: 20px; height: 20px; background: var(--purple); }
  .card--back .brand {
    position: absolute; left: 0; right: 0; top: 186px;
    justify-content: center; color: var(--white); font-size: 38px;
  }
  .card--back .brand__dot { width: 46px; height: 46px; background: var(--white); }

  .divider {
    position: absolute; left: 262px; top: 64px;
    width: 1px; height: 237px; background: #c4c4c4;
  }
  .details {
    position: absolute; left: 279px; top: 58px;
    color: var(--grey-text); font-size: 17px; line-height: 21px;
  }
  .doctor { color: var(--purple); font-weight: 600; font-size: 18.5px; line-height: 23.5px; }
  .doctor .degree { color: var(--grey-muted); font-weight: 600; font-size: 16px; }
  .doctors { margin-bottom: 7px; }
  .office { margin-bottom: 11px; font-style: normal; }
  .line { display: flex; align-items: center; gap: 4px; white-space: nowrap; }
  .icon { width: 13px; height: 13px; flex: none; fill: var(--purple); }
  .web-domain { color: var(--purple); }

  .edge-band {
    position: absolute; left: 0; right: 0; bottom: 0; height: 8px;
    display: flex;
  }
  .edge-band__silver { width: 255px; background: var(--silver); }
  .edge-band__gap { width: 3px; background: var(--white); }
  .edge-band__purple { flex: 1; background: var(--purple); }
</style>
</head>
<body>

<section class="card card--front">
  <div class="brand">
    <span class="brand__dot"></span>
    <span class="brand__name">Halvercott Orthodontics</span>
  </div>

  <div class="divider"></div>

  <div class="details">
    <div class="doctors">
      <p class="doctor">Marguerite L. Halvercott<span class="degree">, DMD</span></p>
      <p class="doctor">Douglas R. Halvercott<span class="degree">, DMD</span></p>
    </div>

    <address class="office">
      <p>312 Bramblewood Street</p>
      <p>North Andover, MA 01899</p>
      <p class="line">
        <svg class="icon" viewBox="0 0 24 24" aria-hidden="true"><path d="M6.6 10.8a15.1 15.1 0 0 0 6.6 6.6l2.2-2.2a1 1 0 0 1 1-.25 11.4 11.4 0 0 0 3.6.57 1 1 0 0 1 1 1V20a1 1 0 0 1-1 1A17 17 0 0 1 3 4a1 1 0 0 1 1-1h3.5a1 1 0 0 1 1 1c0 1.25.2 2.45.57 3.57a1 1 0 0 1-.25 1z"/></svg>
        <span>978.555.0142</span>
      </p>
    </address>

    <address class="office">
      <p>847C Quarry Hollow Street</p>
      <p>Methuen, MA 01898</p>
      <p class="line">
        <svg class="icon" viewBox="0 0 24 24" aria-hidden="true"><path d="M6.6 10.8a15.1 15.1 0 0 0 6.6 6.6l2.2-2.2a1 1 0 0 1 1-.25 11.4 11.4 0 0 0 3.6.57 1 1 0 0 1 1 1V20a1 1 0 0 1-1 1A17 17 0 0 1 3 4a1 1 0 0 1 1-1h3.5a1 1 0 0 1 1 1c0 1.25.2 2.45.57 3.57a1 1 0 0 1-.25 1z"/></svg>
        <span>978.555.0187</span>
      </p>
    </address>

    <p class="line">
      <svg class="icon" viewBox="0 0 24 24" aria-hidden="true"><path d="M2 5h20v14H2z M2 5l10 8 10-8" fill="var(--purple)" stroke="#fff" stroke-width="1.5"/></svg>
      <span>frontdesk@halvercottortho.example</span>
    </p>
    <p class="line">
      <svg class="icon" viewBox="0 0 24 24" aria-hidden="true"><circle cx="12" cy="12" r="10" fill="none" stroke="var(--purple)" stroke-width="2"/><path d="M2 12h20M12 2c3 3 3 17 0 20M12 2c-3 3-3 17 0 20" fill="none" stroke="var(--purple)" stroke-width="1.6"/></svg>
      <span>www.<span class="web-domain">halvercottortho</span>.example</span>
    </p>
  </div>

  <div class="edge-band">
    <span class="edge-band__silver"></span>
    <span class="edge-band__gap"></span>
    <span class="edge-band__purple"></span>
  </div>
</section>

<section class="card card--back">
  <div class="brand">
    <span class="brand__dot"></span>
    <span class="brand__name">Halvercott Orthodontics</span>
  </div>
</section>

</body>
</html>
```